Web Design Project - vR Advise

We want to modernise our web page profile. We have an existing web site that we are particularly not proud of (www.vradvise.com.au).
We have started to build a new web site using Plivex and we like the structure of it, but we need it to be professionally designed and implemented.

This current development site can be viewed here: dev.vradvise.com.au

We would like a complete design for the entire website, ready for deployment.

(We still need to finalise the content, as we have just developed new products that we hope to launch in August both on this web site and by a Vendor Forum.)
Updates

Reason: Project must be complete by this friday at the latest.

Target Market(s)

Larger companies where the robustness of their IT infrastructure is critical. Our tools and services provide for monitoring of every device

Industry/Entity Type

Build

Requirements
Must have
• Responsive design for different screen sizes.

BrightDock help desk software integrated with the website.
Currently can be viewed at support.vradvise.com.au
Brightdock only supports custom css.

Nice to have
• Customer experience testimonials in a rotating banner
Chirply and Pagebook links in the footer
We use Avenir as a company font.
Use company colours as in the logo (green and blue)

```html
<!DOCTYPE html>
<html lang="en">
<head>
<meta charset="utf-8">
<title>vR Advise — Home</title>
<link href="https://fonts.googleapis.com/css2?family=Nunito+Sans:wght@300;400;600;700;800;900&display=swap" rel="stylesheet">
<style>
:root{
  --blue:#2b73b0;
  --blue-dark:#1f5f97;
  --blue-footer:#2f73ad;
  --green:#8cbf26;
  --green-dark:#6fa012;
  --grey-text:#666d73;
  --band:#eceef0;
  --line:#d4d8dc;
  --white:#ffffff;
}
*{margin:0;padding:0;box-sizing:border-box}
html,body{width:1200px;height:961px;overflow:hidden}
body{position:relative;font-family:"Nunito Sans",Arial,sans-serif;background:#f7f8fa;color:var(--grey-text)}
.abs{position:absolute}

.topbar{left:0;top:0;width:1200px;height:6px;background:var(--blue)}
.utility{left:848px;top:6px;width:148px;height:22px;background:var(--blue);clip-path:polygon(14px 0,100% 0,100% 100%,26px 100%);display:flex;align-items:center;justify-content:flex-end;gap:10px;padding-right:12px}
.utility svg{width:14px;height:14px}
.utility .flag{width:14px;height:14px;border-radius:50%;background:#e8ecf2}

.hero{left:0;top:6px;width:1200px;height:376px;background:linear-gradient(90deg,#dde6ee 0%,#eef2f5 40%,#e6ecf1 75%,#d8e2ea 100%)}
.hero-visual{left:544px;top:112px;width:448px;height:270px;background:radial-gradient(ellipse at 72% 55%,#f4f6f8 0%,#cfd9e2 55%,rgba(220,229,236,0) 80%)}

.social{display:flex;gap:4px}
.social span{width:22px;height:22px;border-radius:50%;display:block}
.social .s1{background:#3aa3e0}.social .s2{background:#3b5a9a}.social .s3{background:#3a3a3a}
.social-top{left:922px;top:44px}

.brand{left:208px;top:64px;display:flex;align-items:center;gap:10px}
.brand .dot{width:34px;height:34px;border-radius:50%;background:var(--green)}
.brand .name{font-size:32px;font-weight:800;color:var(--blue);letter-spacing:-.5px}

.nav{left:553px;top:78px;display:flex;align-items:center;font-size:13px;font-weight:600;color:var(--blue);letter-spacing:.1px}
.nav a{color:inherit;text-decoration:none;padding:0 7px;position:relative;height:24px;line-height:18px}
.nav a + a::before{content:"";position:absolute;left:-1px;top:4px;height:10px;border-left:1px dotted #8aa}
.nav .active{border-bottom:3px solid var(--blue)}
.nav-rule{left:470px;top:104px;width:560px;height:1px;background:linear-gradient(90deg,rgba(160,175,190,0),#a8b6c4,rgba(160,175,190,0))}

.headline{left:198px;top:164px;font-size:25px;line-height:27px;font-weight:900;color:var(--blue);letter-spacing:-1.4px}
.headline em{font-style:normal;color:var(--green)}
.intro{left:198px;top:260px;width:340px;font-size:9.6px;line-height:16.4px;color:#5e656b;text-transform:uppercase}
.quote-btn{left:200px;top:323px;width:170px;height:32px;border-radius:16px;background:linear-gradient(#a6d03a,var(--green-dark));box-shadow:0 0 0 3px rgba(255,255,255,.8);color:#fff;font-size:11.5px;font-weight:800;display:flex;align-items:center}
.quote-btn .label{flex:1;padding-left:19px;letter-spacing:-.2px}
.quote-btn .arrow{width:38px;height:100%;border-left:1px solid rgba(255,255,255,.35);display:flex;align-items:center;justify-content:center}

.lead-form{left:0;top:382px;width:1200px;height:52px;background:linear-gradient(#f7f8f9,#e4e7ea);border-top:1px solid #fff;border-bottom:1px solid var(--line)}
.field{top:15px;height:25px;display:flex;background:#fff;border:1px solid #d6dadd}
.field .ico{width:37px;background:var(--blue);display:flex;align-items:center;justify-content:center}
.field .ico svg{width:14px;height:14px}
.field .ph{padding-left:13px;font-size:9px;line-height:23px;color:#9aa2a8;letter-spacing:.3px}
.f-name{left:197px;width:173px}.f-mail{left:414px;width:176px}.f-phone{left:627px;width:174px}
.sep{top:22px;height:14px;border-left:1px dotted #999}
.submit{left:845px;top:12px;width:134px;height:30px;border-radius:15px;background:linear-gradient(#a6d03a,var(--green-dark));box-shadow:0 0 0 3px rgba(255,255,255,.9);color:#fff;font-size:14px;font-weight:800;text-align:center;line-height:30px;letter-spacing:-.3px}
.submit-rule{left:822px;top:6px;height:40px;border-left:1px solid #cfd3d7}

.services{left:0;top:434px;width:1200px;height:216px;background:#fdfdfe}
.service{top:56px;width:250px}
.service .head{display:flex;align-items:flex-start;gap:8px}
.service-icon{width:46px;height:46px;flex:none;border-radius:6px;background:linear-gradient(135deg,#d5e3ef,#e3efcf)}
.service h3{font-size:14.4px;line-height:17px;font-weight:800;color:var(--blue);padding-left:9px;border-left:1px dotted #9aa;letter-spacing:.1px;text-transform:uppercase}
.service p{margin-top:12px;font-size:10.4px;line-height:14.4px;color:var(--grey-text)}
.read-more{display:inline-block;margin-top:8px;width:72px;height:22px;border-radius:11px;background:var(--blue);color:#fff;font-size:8.5px;font-weight:800;text-align:center;line-height:22px}
.sv1{left:198px}.sv2{left:475px}.sv3{left:751px}
.sv1 p,.sv2 p{width:200px}
.sv3 p{width:248px}

.testimonials{left:0;top:651px;width:1200px;height:147px;background:#f6f7f9;border-top:1px solid #e3e6e9}
.testimonial{top:34px;width:240px;height:80px}
.avatar{left:0;top:0;width:76px;height:76px;border-radius:50%;background:radial-gradient(circle at 50% 40%,#d9c3b0,#8a7a6e 70%);border:4px solid #fff;box-shadow:0 1px 4px rgba(0,0,0,.25)}
.bubble{left:74px;top:18px;width:150px;height:30px;background:var(--blue);color:#cfe0ef;font-size:8.4px;line-height:10.5px;padding:5px 0 0 10px}
.qmark{left:224px;top:26px;width:16px;height:16px;background:#fff;border:1px solid #d3d7db;color:var(--blue);font-size:14px;font-weight:900;line-height:18px;text-align:center}
.byline{left:74px;top:48px;width:150px;height:19px;background:#fff;border:1px solid #d3d7db;display:flex;align-items:center;font-size:8.4px;font-weight:800;color:#222}
.byline svg{width:8px;height:8px;margin:0 6px 0 8px}
.byline .stars{margin-left:auto;padding:0 4px 0 6px;border-left:1px dotted #999;color:#e0b84a;font-size:7.5px;letter-spacing:.5px}
.t1{left:198px}.t2{left:476px}.t3{left:754px}

.partners{left:0;top:798px;width:1200px;height:60px;background:linear-gradient(#f8f9fa,#e7e9ec);border-top:1px solid #dfe2e5}
.partners h2{position:absolute;left:202px;top:18px;font-size:19.5px;font-weight:900;color:var(--blue);letter-spacing:-.8px}
.partners .rule{position:absolute;left:382px;top:8px;height:44px;border-left:1px solid #cfd3d7}
.badge{position:absolute;background:#c9ced4}
.b1{left:422px;top:9px;width:26px;height:40px;background:#2f3a73}
.b2{left:514px;top:17px;width:118px;height:26px;border-radius:4px;background:#4f5560}
.b3{left:696px;top:19px;width:106px;height:20px;border-radius:4px;background:#7d8187}
.b4{left:874px;top:11px;width:92px;height:36px;border-radius:4px;background:#1f3f78}

.footer{left:0;top:858px;width:1200px;height:103px;background:var(--blue-footer);color:#fff}
.footer h4{position:absolute;font-size:15px;font-weight:900;letter-spacing:-.4px;text-transform:uppercase}
.f-about h4{left:199px;top:16px}
.f-about p{position:absolute;left:199px;top:40px;width:200px;font-size:9.6px;line-height:11.6px;color:#e6eef6}
.f-connect h4{left:544px;top:14px}
.f-connect .social{position:absolute;left:572px;top:38px}
.f-contact h4{left:822px;top:18px}
.f-contact .role{position:absolute;left:823px;top:36px;font-size:10.5px;font-weight:800}
.f-contact dl{position:absolute;left:823px;top:53px;display:grid;grid-template-columns:45px auto;font-size:9.6px;line-height:12px}
.f-links{left:198px;top:80px;font-size:9.6px;color:#eef4fa}
.f-copy{left:611px;top:80px;font-size:9.6px;color:#eef4fa}
</style>
</head>
<body>

<div class="abs hero"></div>
<div class="abs hero-visual" role="img" aria-label="Photo of a smiling businessman holding a small globe surrounded by networked computers"></div>
<div class="abs topbar"></div>

<div class="abs utility">
  <svg viewBox="0 0 14 14" fill="none" stroke="#fff" stroke-width="1.5"><path d="M2 7 7 2.5 12 7M3.5 6v5.5h7V6"/></svg>
  <svg viewBox="0 0 14 14" fill="none" stroke="#fff" stroke-width="1.4"><rect x="1.5" y="3" width="11" height="8"/><path d="M1.5 3 7 8l5.5-5"/></svg>
  <svg viewBox="0 0 14 14" fill="#fff"><rect x="1.5" y="3" width="11" height="9" rx="1"/><rect x="3" y="5" width="4" height="5" fill="#2b73b0"/></svg>
  <span class="flag"></span>
</div>

<div class="abs social social-top"><span class="s1"></span><span class="s2"></span><span class="s3"></span></div>

<div class="abs brand"><span class="dot"></span><span class="name">vR Advise</span></div>

<nav class="abs nav">
  <a class="active">HOME</a><a>SERVICES</a><a>SOLUTIONS</a><a>PARTNERS</a><a>ABOUT US</a><a>CONTACT</a>
</nav>
<div class="abs nav-rule"></div>

<h1 class="abs headline">DEDICATED TO MAKING<br>BUSINESS SENSE OF <em>IT</em><br>CHALLENGES.</h1>
<p class="abs intro">We are an organisation that prides itself on attracting, employing, retaining and developing subject matter experts in the field of consulting.</p>
<div class="abs quote-btn"><span class="label">REQUEST A QUOTE</span><span class="arrow"><svg width="10" height="16" viewBox="0 0 10 16" fill="none" stroke="#fff" stroke-width="1.6"><path d="M2 2l6 6-6 6"/></svg></span></div>

<form class="abs lead-form">
  <div class="abs field f-name"><span class="ico"><svg viewBox="0 0 14 14" fill="#fff"><circle cx="7" cy="4.5" r="3"/><path d="M1.5 13c0-3 2.5-5 5.5-5s5.5 2 5.5 5z"/></svg></span><span class="ph">ENTER YOUR NAME</span></div>
  <div class="abs sep" style="left:392px"></div>
  <div class="abs field f-mail"><span class="ico"><svg viewBox="0 0 14 14" fill="none" stroke="#fff" stroke-width="1.4"><rect x="1.5" y="3" width="11" height="8"/><path d="M1.5 3 7 8l5.5-5"/></svg></span><span class="ph">YOUR EMAIL ADDERESS</span></div>
  <div class="abs sep" style="left:607px"></div>
  <div class="abs field f-phone"><span class="ico"><svg viewBox="0 0 14 14" fill="#fff"><rect x="1.5" y="3" width="11" height="9" rx="1"/><rect x="3" y="5" width="4" height="5" fill="#2b73b0"/></svg></span><span class="ph">YOUR PHONE NUMBER</span></div>
  <div class="abs submit-rule"></div>
  <div class="abs submit">SUBMIT NOW</div>
</form>

<section class="abs services">
  <div class="abs service sv1">
    <div class="head">
      <div class="service-icon" role="img" aria-label="Consulting service illustration"></div>
      <h3>IT Consulting<br>Services</h3>
    </div>
    <p>Lorem ipsum dolor sit amet, consectetuer adipiscing elit, sed diam nonummy nibh euismod tincidunt ut laoreet dolore.</p>
    <span class="read-more">READ MORE</span>
  </div>
  <div class="abs service sv2">
    <div class="head">
      <div class="service-icon" role="img" aria-label="Architecture service illustration"></div>
      <h3>IT Architecture<br>Services</h3>
    </div>
    <p>Lorem ipsum dolor sit amet, consectetuer adipiscing elit, sed diam nonummy nibh euismod tincidunt ut laoreet dolore.</p>
    <span class="read-more">READ MORE</span>
  </div>
  <div class="abs service sv3">
    <div class="head">
      <div class="service-icon" role="img" aria-label="Support service illustration"></div>
      <h3>Professional Service<br>and Support</h3>
    </div>
    <p>Lorem ipsum dolor sit amet, consectetuer adipiscing elit, sed diam nonummy nibh euismod tincidunt ut laoreet dolore.</p>
    <span class="read-more">READ MORE</span>
  </div>
</section>

<section class="abs testimonials">
  <div class="abs testimonial t1">
    <div class="abs bubble">Lorem ipsum dolor sit amet,<br>consectetuer adipiscing elit, sed.</div>
    <div class="abs qmark">”</div>
    <div class="abs byline"><svg viewBox="0 0 8 8" fill="#2b73b0"><circle cx="4" cy="2.2" r="2"/><path d="M0 8c0-2.5 1.8-4 4-4s4 1.5 4 4z"/></svg>LOREM IPSUM<span class="stars">★★★★★</span></div>
    <div class="abs avatar" role="img" aria-label="Client portrait photo"></div>
  </div>
  <div class="abs testimonial t2">
    <div class="abs bubble">Lorem ipsum dolor sit amet,<br>consectetuer adipiscing elit, sed.</div>
    <div class="abs qmark">”</div>
    <div class="abs byline"><svg viewBox="0 0 8 8" fill="#2b73b0"><circle cx="4" cy="2.2" r="2"/><path d="M0 8c0-2.5 1.8-4 4-4s4 1.5 4 4z"/></svg>LOREM IPSUM<span class="stars">★★★★★</span></div>
    <div class="abs avatar" role="img" aria-label="Client portrait photo"></div>
  </div>
  <div class="abs testimonial t3">
    <div class="abs bubble">Lorem ipsum dolor sit amet,<br>consectetuer adipiscing elit, sed.</div>
    <div class="abs qmark">”</div>
    <div class="abs byline"><svg viewBox="0 0 8 8" fill="#2b73b0"><circle cx="4" cy="2.2" r="2"/><path d="M0 8c0-2.5 1.8-4 4-4s4 1.5 4 4z"/></svg>LOREM IPSUM<span class="stars">★★★★★</span></div>
    <div class="abs avatar" role="img" aria-label="Client portrait photo"></div>
  </div>
</section>

<section class="abs partners">
  <h2>OUR PARTNERS:</h2>
  <span class="rule"></span>
  <span class="badge b1" role="img" aria-label="Partner badge"></span>
  <span class="badge b2" role="img" aria-label="Partner badge"></span>
  <span class="badge b3" role="img" aria-label="Partner badge"></span>
  <span class="badge b4" role="img" aria-label="Partner badge"></span>
</section>

<footer class="abs footer">
  <div class="f-about">
    <h4>About Us</h4>
    <p>Lorem ipsum dolor sit amet, consectetuer adipiscing elit, sed diam nonummy nibh euismod tincidunt.</p>
  </div>
  <div class="f-connect">
    <h4>Connect With Us</h4>
    <div class="social" aria-label="Chirply, Pagebook and other social links"><span class="s1"></span><span class="s2"></span><span class="s3"></span></div>
  </div>
  <div class="f-contact">
    <h4>Dana Morrell</h4>
    <div class="role">SALES &amp; MARKETING DIRECTOR</div>
    <dl>
      <dt>Mobile:</dt><dd>+61 (0) 400 555 01</dd>
      <dt>Email:</dt><dd>dana.morrell@vradvise.com.au</dd>
      <dt>Web:</dt><dd>www.vradvise.com.au</dd>
    </dl>
  </div>
  <div class="abs f-links">HOME | ABOUT US | PATENT PENDING | COPY RIGHT | PRIVACY | CONTACT US PRIVACY</div>
  <div class="abs f-copy">2013 VRADVISE, ALL RIGHTS RESERVED.</div>
</footer>

</body>
</html>
```